Fish Farm needing 3 - Fold Flyer / Price List designed

We are looking for a new Price List for our Fish Farm. I have attached an example of the basic info that needs in the flyer. We want the flyer to be a 3 fold page. Anything that is on our website, you can use for ideas. There are some pictures on there that can be photoshopped into the flyer. Do not use any photos from any other sites. We are looking for something professional but fun and exciting! I have also attached our business logo. We tend to stay with the blues and greens for colors. Let's get started....
Updates

Need extra days to review

Contact Information for Business Card

We are needing a business card with our new logo on it. We also need our address, phone numbers, email address, and website listed. Please view our website for more ideas.

Colors

Designer to choose colors to be used in the design.

```html
<!DOCTYPE html>
<html lang="en">
<head>
<meta charset="utf-8">
<title>Kestrel Pond Fish Farm — Tri-fold Price List</title>
<link href="https://fonts.googleapis.com/css2?family=Poppins:wght@400;500;600;700;800&display=swap" rel="stylesheet">
<style>
  :root{
    --page:#e4e5ec;
    --royal:#2b2fa6;
    --royal-deep:#1d2088;
    --night:#141a6e;
    --lime:#7cba3d;
    --lime-dark:#5f9c2a;
    --gold:#f2b632;
    --white:#ffffff;
    --photo-warm:#7a6a55;
    --photo-cool:#4b5a7a;
    --glass:rgba(255,255,255,.18);
  }
  *{box-sizing:border-box;margin:0;padding:0}
  html,body{width:900px;height:1200px;overflow:hidden}
  body{background:var(--page);font-family:"Poppins",sans-serif;color:var(--white);position:relative}

  .spread{position:absolute;left:60px;width:780px;height:555px;overflow:hidden;box-shadow:0 10px 30px rgba(20,20,60,.25)}
  .spread--outside{top:35px;background:var(--royal)}
  .spread--inside{top:620px;background:var(--night)}
  .spread__art{position:absolute;inset:0}
  .panel{position:absolute;top:0;width:260px;height:555px}
  .panel--left{left:0}.panel--middle{left:260px}.panel--right{left:520px}

  /* outside — left */
  .contact-note{position:absolute;left:22px;top:70px;width:216px;font-size:10.5px;line-height:1.5;text-align:center}
  .contact-note p{margin-bottom:9px}
  .map-area{position:absolute;left:22px;top:300px;width:216px;height:230px;border-radius:4px;background:linear-gradient(160deg,#3a3fb4,#2a2e9c)}

  /* outside — middle */
  .stocking{position:absolute;left:0;top:0;width:260px;height:555px;text-align:center}
  .stocking__mark{width:46px;height:46px;border-radius:50%;border:3px solid var(--white);margin:70px auto 0}
  .stocking__title{margin-top:22px;font-size:21px;line-height:1.15;font-weight:700;color:var(--royal-deep)}
  .stocking__sub{margin-top:12px;font-size:13px;font-weight:700;color:var(--royal-deep);letter-spacing:.5px}
  .stocking__list{list-style:none;margin-top:22px;font-size:10.5px;font-weight:600;line-height:1.75}
  .stocking__mark--low{margin-top:50px}

  /* outside — right */
  .brand{position:absolute;left:0;top:0;width:260px;height:62px;display:flex;align-items:center;justify-content:center;gap:8px}
  .brand__dot{width:12px;height:12px;border-radius:50%;background:var(--royal)}
  .brand__name{font-size:17px;font-weight:700;color:var(--royal)}
  .pricelist{position:absolute;left:0;top:78px;width:260px;text-align:center}
  .pricelist__title{font-size:15px;font-weight:700;letter-spacing:.5px}
  .pricelist__items{list-style:none;margin-top:8px;font-size:10.5px;font-weight:600;line-height:1.45}
  .company{position:absolute;left:0;top:380px;width:260px;text-align:center}
  .company__name{font-size:17px;font-weight:700;line-height:1.15}
  .company__address{font-size:10px;margin-top:4px}
  .company__phones{margin:12px auto 0;font-size:9.5px;line-height:1.6;display:grid;grid-template-columns:auto auto;column-gap:16px;justify-content:center;text-align:left}
  .company__links{position:absolute;left:0;bottom:16px;width:260px;display:flex;justify-content:space-around;font-size:8.5px}

  /* inside */
  .price{position:absolute;text-align:center;z-index:2}
  .price__head{font-size:13px;font-weight:700;color:var(--gold);line-height:1.15}
  .price__note{font-size:9px;color:var(--gold);font-weight:500}
  .price__box{margin:6px auto 10px;background:var(--glass);border-radius:8px;padding:6px 10px;font-size:9px;line-height:1.55;display:inline-grid;column-gap:14px;text-align:left}
  .cols-2{grid-template-columns:auto auto}
  .cols-3{grid-template-columns:auto auto auto}
  .cols-4{grid-template-columns:auto auto auto auto}
  .price__plain{font-size:9px;line-height:1.5;margin:3px 0 8px}
  .price__big{font-size:15px;color:var(--gold);font-weight:600}
  .fineprint{font-size:8px;line-height:1.4;text-align:center}
  .koi-block{left:8px;top:312px;width:160px}
  .koi-callout{font-size:15px;font-weight:800;color:var(--gold);line-height:1.15;margin-top:2px}
  .koi-callout__sub{font-size:8px;font-weight:500;margin-top:3px}
  .koi-photo{position:absolute;right:0;bottom:0;width:96px;height:170px;background:linear-gradient(180deg,#2f52b8 0%,#d98a2a 70%,#b5642a 100%);border-top-left-radius:48px;z-index:1}
</style>
</head>
<body>

<!-- OUTSIDE -->
<section class="spread spread--outside">
  <svg class="spread__art" width="780" height="555" viewBox="0 0 780 555">
    <rect x="260" y="0" width="260" height="555" fill="var(--lime)"/>
    <path d="M0 30 Q130 10 260 20 V250 Q140 275 0 300 Z" fill="var(--photo-cool)" role="img" aria-label="Photo of the farm owner standing by a pond"/>
    <path d="M0 300 Q140 275 260 250" stroke="var(--lime)" stroke-width="5" fill="none"/>
    <path d="M0 30 Q130 10 260 20" stroke="var(--lime)" stroke-width="4" fill="none"/>
    <path d="M260 20 Q390 40 520 0 V0 H260 Z" fill="var(--royal)"/>
    <path d="M520 40 H780 V300 Q650 330 520 345 Z" fill="var(--photo-warm)" role="img" aria-label="Photo of the farm owner holding a fish at the pond"/>
    <path d="M520 345 Q650 330 780 300" stroke="var(--lime)" stroke-width="5" fill="none"/>
    <path d="M520 0 H780 V40 Q650 75 520 62 Z" fill="var(--white)"/>
    <path d="M520 62 Q650 75 780 40" stroke="var(--lime)" stroke-width="4" fill="none"/>
  </svg>

  <div class="panel panel--left">
    <div class="contact-note">
      <p>Feel free to call the farm or the cell phone; if no answer, leave a message and we will get back to you as soon as possible.</p>
      <p>Always call before coming to the farm as we may be on a delivery.</p>
      <p>Our Sales Route Schedule is listed on our website at:</p>
      <p>www.kestrelpondfish.com/schedule</p>
    </div>
    <div class="map-area" role="img" aria-label="Road map showing directions to the farm"></div>
  </div>

  <div class="panel panel--middle">
    <div class="stocking">
      <div class="stocking__mark"></div>
      <h2 class="stocking__title">STANDARD<br>STOCKING RATES</h2>
      <p class="stocking__sub">PER SURFACE ACRE</p>
      <ul class="stocking__list">
        <li>600-1,000 HYBRID BLUEGILL,</li>
        <li>REGULAR BLUEGILL, OR REDEAR</li>
        <li>100-200 LARGEMOUTH BASS</li>
        <li>100-200 CHANNEL CATFISH</li>
        <li>3,000-5,000 FATHEAD MINNOWS</li>
      </ul>
      <div class="stocking__mark stocking__mark--low"></div>
    </div>
  </div>

  <div class="panel panel--right">
    <div class="brand"><span class="brand__dot"></span><span class="brand__name">Kestrel Pond Fish Farm</span></div>
    <div class="pricelist">
      <h2 class="pricelist__title">2019 PRICE LIST FOR:</h2>
      <ul class="pricelist__items">
        <li>HYBRID BLUEGILL</li><li>REGULAR BLUEGILL</li><li>REDEAR SUNFISH</li>
        <li>LARGEMOUTH BASS</li><li>FATHEAD MINNOWS</li><li>GOLDEN SHINERS</li>
        <li>TRIPLOID GRASS CARP</li><li>CHANNEL CATFISH</li><li>ALBINO CATFISH</li>
        <li>BLACK CRAPPIE</li><li>JAPANESE KOI</li><li>TILAPIA</li><li>FISH FOOD</li>
      </ul>
    </div>
    <div class="company">
      <h3 class="company__name">KESTREL POND<br>FISH FARM, LLC</h3>
      <p class="company__address">2280 Willow Bend Rd<br>Marston, IN 47000</p>
      <div class="company__phones">
        <span>FARM</span><span>(555) 201-4410</span>
        <span>CELL</span><span>(555) 201-4412</span>
        <span>TEXT</span><span>(555) 201-4415</span>
      </div>
    </div>
    <div class="company__links"><span>/kestrelpondfish</span><span>www.kestrelpondfish.com</span></div>
  </div>
</section>

<!-- INSIDE -->
<section class="spread spread--inside">
  <svg class="spread__art" width="780" height="555" viewBox="0 0 780 555">
    <defs>
      <linearGradient id="water" x1="0" y1="0" x2="0" y2="1">
        <stop offset="0" stop-color="#1f2a8e"/><stop offset=".6" stop-color="#2a3ab0"/><stop offset="1" stop-color="#1a1f7a"/>
      </linearGradient>
    </defs>
    <rect width="780" height="555" fill="url(#water)" role="img" aria-label="Photo of a calm pond at dusk"/>
    <path d="M0 470 Q390 420 780 470 V555 H0 Z" fill="#0f1350"/>
    <path d="M0 470 Q390 420 780 470" stroke="var(--lime)" stroke-width="5" fill="none"/>
    <path d="M0 10 Q130 0 260 10" stroke="var(--lime)" stroke-width="3" fill="none" opacity=".8"/>
  </svg>

  <div class="panel panel--left">
    <div class="price" style="left:0;top:14px;width:260px">
      <h3 class="price__head">HYBRID BLUEGILL</h3>
      <p class="price__note">(Hybrid Sunfish)</p>
      <div class="price__box cols-4">
        <span>Size</span><span>Each</span><span>100</span><span>1000</span>
        <span>1-2 inch</span><span>.65</span><span>$60</span><span>$550</span>
        <span>2-3 inch</span><span>.85</span><span>$80</span><span>$750</span>
      </div>
      <h3 class="price__head">REGULAR BLUEGILL</h3>
      <div class="price__box cols-3">
        <span>Size</span><span>Each</span><span>1000</span>
        <span>1-3 inch</span><span>.45</span><span>$400</span>
      </div>
      <h3 class="price__head">REDEAR SUNFISH</h3>
      <div class="price__box cols-3">
        <span>Size</span><span>Each</span><span>1000</span>
        <span>2-3 inch</span><span>.55</span><span>$500</span>
        <span>3-4 inch</span><span>.70</span><span>$650</span>
      </div>
      <h3 class="price__head">LARGEMOUTH BASS</h3>
      <div class="price__box cols-2">
        <span>Size</span><span>Each</span>
        <span>2-3 inch</span><span>$1.00</span>
        <span>3-4 inch</span><span>$1.50</span>
        <span>4-6 inch</span><span>$2.50</span>
        <span>6-8 inch</span><span>$3.75</span>
      </div>
      <p class="fineprint">*WHEN AVAILABLE<br>SIZES VARY DEPENDING ON<br>TIME OF YEAR</p>
    </div>
  </div>

  <div class="panel panel--middle">
    <div class="price" style="left:0;top:30px;width:260px">
      <h3 class="price__head">TRIPLOID GRASS CARP</h3>
      <p class="price__note">(Indiana Prices)</p>
      <div class="price__box cols-2">
        <span>8-11 inch</span><span>Medium</span>
        <span>1-24 Grass Carp</span><span>$14.00 each</span>
        <span>25-99 Grass Carp</span><span>$12.00 each</span>
        <span>100+ Grass Carp</span><span>Inquire</span>
      </div>
      <h3 class="price__head">CHANNEL CATFISH</h3>
      <div class="price__box cols-3">
        <span>Size</span><span>Each</span><span>100</span>
        <span>6-8 inch</span><span>.65</span><span>$60</span>
      </div>
      <h3 class="price__head">ALBINO CATFISH</h3>
      <p class="price__note">(March &amp; April)</p>
      <div class="price__plain">Size &nbsp;&nbsp; Each<br>5-8 inch &nbsp; $1.20</div>
      <h3 class="price__head">BLACK CRAPPIE</h3>
      <p class="price__note">(March &amp; April)</p>
      <div class="price__plain">Size &nbsp;&nbsp; Each<br>3-5 inch &nbsp; $1.50</div>
      <h3 class="price__head">FATHEAD MINNOWS</h3>
      <p class="price__big">$16.00 per thousand</p>
      <p class="price__plain">($9.00 per lb)</p>
    </div>
  </div>

  <div class="panel panel--right">
    <div class="price" style="left:0;top:40px;width:260px">
      <h3 class="price__head">GOLDEN SHINERS</h3>
      <p class="price__note">(Delivery Only – Minimum 50 lb)</p>
      <div class="price__plain">Lb &nbsp;&nbsp; $6.00<br>100 lb &nbsp; $7.50</div>
      <h3 class="price__head">FLOATING FISH FOOD</h3>
      <div class="price__plain">Starter Size (50 lb Bag)<br>40% Protein<br>Market Price – Inquire<br>(Only Available at Farm)</div>
      <h3 class="price__head">TILAPIA</h3>
      <p class="price__note">(May 15 – June 30)</p>
      <div class="price__box cols-2">
        <span>5-10 Tilapia per lb</span><span></span>
        <span>1-25 lb</span><span>$15.00 lb</span>
        <span>26-50 lb</span><span>$14.00 lb</span>
        <span>51-75 lb</span><span>$13.00 lb</span>
        <span>76+ lb</span><span>$12.00 lb</span>
      </div>
    </div>
    <div class="price koi-block">
      <h3 class="price__head">JAPANESE KOI</h3>
      <div class="price__box cols-2">
        <span>Size</span><span>Each</span>
        <span>4-5 inch</span><span>$6.00</span>
        <span>6-8 inch</span><span>$10.00</span>
        <span>9-12 inch</span><span>$15.00</span>
      </div>
      <p class="koi-callout">BUTTERFLY KOI<br>ALSO AVAILABLE!</p>
      <p class="koi-callout__sub">Butterfly koi also available</p>
    </div>
    <div class="koi-photo" role="img" aria-label="Photo of the farm owner holding a large orange koi"></div>
  </div>
</section>

</body>
</html>
```